National Human Immunology Network Needs a Brochure DesignBrochure Design Project

We need a brochure design for a new Canadian network called VEKO. VEKO stands for "VRSL Cellular Defence Alliance". (VRSL is the Northfield Councils of Medical Inquiry and is the funder of the network).

The VRSL Cellular Defence Alliance (VEKO) is a resource network that facilitates, promotes and enhances research in human immunology and its translation into clinical care and public policy. VEKO is an inclusive National Network with International projections that will act as a coordinating resource for investigators working in different aspects of Human Immunology. As a research network, VEKO will operate as a resource “umbrella” network, facilitating communication between nodes, each with their specialized expertise in human immunology,
collaboration and knowledge exchange.

We have a VEKO logo already designed as well as the text to be used in the brochure. In addition we should include the VRSL logo somewhere on the brochure, but it does need to be front and centre. Thinking that a tri-fold brochure would work best.

Target Market(s)

Researchers, politicians, lay public

Industry/Entity Type

Communication

Requirements
Must have
• Must use logo provided.

```html
<!DOCTYPE html>
<html lang="en">
<head>
<meta charset="utf-8">
<title>VEKO Brochure – Back Panel</title>
<link rel="stylesheet" href="https://fonts.googleapis.com/css2?family=Open+Sans:wght@300;400;700&display=swap">
<style>
  :root {
    --stage: #e6e6e6;
    --red-deep: #a3112a;
    --red-mid: #c92a42;
    --red-light: #e36277;
    --accent: #d8202f;
    --ink: #555555;
    --paper: #ffffff;
    --dot: #e0424f;
  }
  * { box-sizing: border-box; margin: 0; padding: 0; }
  html, body {
    width: 1200px; height: 900px; overflow: hidden;
    background: var(--stage);
    font-family: "Open Sans", sans-serif;
  }
  .panel {
    position: absolute; left: 380px; top: 20px;
    width: 440px; height: 860px;
    overflow: hidden;
    box-shadow: 0 6px 22px rgba(0,0,0,.18);
  }
  .panel-photo {
    position: absolute; inset: 0;
    background:
      radial-gradient(circle at 70% 20%, var(--red-light) 0%, transparent 45%),
      radial-gradient(circle at 20% 60%, var(--red-mid) 0%, transparent 55%),
      linear-gradient(160deg, var(--red-mid), var(--red-deep));
  }
  .mission {
    position: absolute; left: 42px; right: 34px; top: 40px;
    color: var(--paper);
    font-weight: 700; font-size: 14px; line-height: 1.45;
    letter-spacing: .06em; text-transform: uppercase;
    text-align: justify;
  }
  .contact-card {
    position: absolute; left: 0; top: 250px; bottom: 0;
    width: 350px;
    background: var(--paper);
    border-top-right-radius: 18px 8px;
    padding: 24px 26px 0 30px;
  }
  .contact-group { padding-bottom: 14px; margin-bottom: 16px; border-bottom: 2px dotted var(--dot); }
  .contact-group:last-of-type { border-bottom: none; }
  .label {
    color: var(--accent); font-weight: 700; font-size: 14px;
    text-transform: uppercase; line-height: 1.2;
  }
  .value { color: var(--ink); font-weight: 300; font-size: 15px; line-height: 1.35; margin-bottom: 6px; }
  .address .label { font-size: 18px; margin-bottom: 4px; }
  .address .value { font-size: 18px; line-height: 1.4; }
  .partner-marks {
    position: absolute; left: 30px; bottom: 26px;
    display: flex; align-items: center; gap: 34px;
  }
  .mark { display: flex; align-items: center; gap: 7px; color: var(--accent); font-weight: 700; font-size: 16px; }
  .mark-square { width: 14px; height: 14px; background: var(--accent); }
  .mark-funder { color: var(--ink); }
  .mark-circle { width: 14px; height: 14px; border-radius: 50%; background: #5aa83c; }
</style>
</head>
<body>
  <section class="panel">
    <div class="panel-photo" role="img" aria-label="Close-up photograph of water droplets on a red surface"></div>

    <p class="mission">The VRSL Cellular Defence Alliance (VEKO) is a resource network that facilitates, promotes and enhances research in human immunology and its translation into clinical care and public policy.</p>

    <div class="contact-card">
      <div class="contact-group">
        <p class="label">Director:</p>
        <p class="value">Ramon Alcaraz</p>
        <p class="label">Tel:</p>
        <p class="value">555-214-0387</p>
        <p class="label">Email:</p>
        <p class="value">ramon.alcaraz@northgate.edu</p>
      </div>
      <div class="contact-group">
        <p class="label">Manager:</p>
        <p class="value">Delia Marchetti</p>
        <p class="label">Tel:</p>
        <p class="value">555-730-4419</p>
        <p class="label">Email:</p>
        <p class="value">delia.marchetti@med.lakeshore.edu</p>
      </div>
      <div class="contact-group address">
        <p class="label">Mailing Address:</p>
        <p class="value">Centre for Cellular Defence<br>2250 Harbour Rd, Suite 214<br>Lakeshore University<br>Brookfield, ON, Canada&nbsp; K2P 4R7</p>
      </div>

      <div class="partner-marks">
        <span class="mark"><span class="mark-square"></span>VEKO</span>
        <span class="mark mark-funder"><span class="mark-circle"></span>VRSL</span>
      </div>
    </div>
  </section>
</body>
</html>
```